" A Lunar Petal Studio é uma pequena empresa, localizada nos Estados Unidos, especializada em criar produtos personalizados para celebrações, como cake toppers, papelaria para festas e peças em papel, acrílico e madeira cortadas a laser. Cada produto é desenvolvido sob encomenda, com foco em qualidade, delicadeza e atenção aos detalhes, proporcionando uma experiência única e memorável para cada cliente. "

```html
<!DOCTYPE html>
<html lang="pt">
<head>
<meta charset="UTF-8">
<title>Lunar Petal Studio – Marcador</title>
<link rel="stylesheet" href="https://fonts.googleapis.com/css2?family=Cormorant+Garamond:wght@500;600&family=Lato:wght@400&display=swap">
<style>
  :root {
    --page-bg: #efece7;
    --card-blue: #dfe7f5;
    --card-white: #ffffff;
    --brand-brown: #6b4536;
    --brand-pink: #efc3c0;
    --rule-pink: #e8aaa6;
    --check-tone: #c9d4e8;
    --rule-grey: #b9b9b9;
    --ink-soft: #7a6a62;
  }
  * { margin: 0; padding: 0; box-sizing: border-box; }
  html, body { width: 1200px; height: 1200px; overflow: hidden; }
  body {
    background: var(--page-bg);
    font-family: "Lato", sans-serif;
    position: relative;
  }
  .bookmark {
    position: absolute;
    top: 324px;
    width: 228px;
    height: 732px;
    box-shadow: 0 4px 14px rgba(0,0,0,0.12);
  }
  .bookmark--front { left: 372px; background: var(--card-blue); }
  .bookmark--back  { left: 640px; background: var(--card-white); }

  .brand {
    position: absolute;
    left: 0; right: 0;
    text-align: center;
    color: var(--brand-brown);
  }
  .brand__dot {
    display: block;
    margin: 0 auto;
    border-radius: 50%;
    background: var(--brand-pink);
  }
  .brand__name {
    font-family: "Cormorant Garamond", serif;
    font-weight: 600;
    line-height: 1.05;
  }
  .brand__tagline {
    font-family: "Lato", sans-serif;
    font-size: 7px;
    letter-spacing: 0.3px;
    color: var(--ink-soft);
    margin-top: 4px;
  }

  .bookmark--front .brand { top: 46px; }
  .bookmark--front .brand__dot { width: 84px; height: 84px; margin-bottom: 14px; }
  .bookmark--front .brand__name { font-size: 26px; }

  .edge-rule {
    position: absolute;
    top: 0; bottom: 0;
    right: 20px;
    width: 10px;
    border-left: 3px solid var(--rule-pink);
    border-right: 2px solid var(--rule-pink);
  }

  .pattern-band {
    position: absolute;
    left: 0; right: 40px;
    top: 528px;
    height: 72px;
    background: linear-gradient(to bottom, rgba(201,212,232,0.35), var(--check-tone));
  }

  .contact {
    position: absolute;
    left: 18px;
    top: 616px;
    list-style: none;
    font-size: 9px;
    color: var(--brand-brown);
  }
  .contact li { display: flex; align-items: center; gap: 6px; margin-bottom: 6px; }
  .contact svg { width: 10px; height: 10px; flex: none; }

  .note-lines {
    position: absolute;
    top: 72px;
    left: 37px;
    right: 37px;
    list-style: none;
  }
  .note-lines li {
    height: 48px;
    border-top: 1px solid var(--rule-grey);
  }
  .note-lines li:last-child { height: 0; }

  .bookmark--back .brand { top: 492px; }
  .bookmark--back .brand__dot { width: 76px; height: 76px; margin-bottom: 10px; }
  .bookmark--back .brand__name { font-size: 20px; }
</style>
</head>
<body>
  <section class="bookmark bookmark--front" aria-label="Marcador, frente">
    <div class="brand">
      <span class="brand__dot"></span>
      <p class="brand__name">Lunar Petal<br>Studio</p>
      <p class="brand__tagline">Custom Party and Laser Crafts</p>
    </div>
    <div class="edge-rule"></div>
    <div class="pattern-band" role="img" aria-label="Faixa decorativa xadrez em azul claro"></div>
    <ul class="contact">
      <li>
        <svg viewBox="0 0 10 10" aria-hidden="true"><path d="M2 1 L3.6 1 L4.2 3 L3.2 3.8 Q4 5.8 6.2 6.8 L7 5.8 L9 6.4 L9 8 Q8.6 9 7.6 9 Q1 8.4 1 2 Q1 1 2 1 Z" fill="none" stroke="currentColor" stroke-width="0.9"/></svg>
        (555) 014-2271
      </li>
      <li>
        <svg viewBox="0 0 10 10" aria-hidden="true"><circle cx="5" cy="5" r="4" fill="none" stroke="currentColor" stroke-width="0.9"/></svg>
        @lunarpetal.studio
      </li>
    </ul>
  </section>

  <section class="bookmark bookmark--back" aria-label="Marcador, verso">
    <ul class="note-lines">
      <li></li><li></li><li></li><li></li><li></li><li></li><li></li>
    </ul>
    <div class="brand">
      <span class="brand__dot"></span>
      <p class="brand__name">Lunar Petal Studio</p>
      <p class="brand__tagline">Custom Party and Laser Crafts</p>
    </div>
  </section>
</body>
</html>
```